Design Challege - Simplify a Complex Message

We have a new website design, but one of the pages presents a particular problem.

Our company does ERP implementations. We have developed a proprietary approach to these implementations based on the idea that you must get eight (and only eight) things right. These eight things are listed below, summarized in one or two words each:

1. Value
2. Capability
3. Functionality
4. Data
5. Technology
6. Change Leadership
7. Quality
8. Governance

Each of these eight things can be summarized in a short paragraph, but when you combine all eight summaries with a brief introductory text, the result is a lot of text - so much text that the casual surfer may be overwhelmed by it.

The winning design will find an engaging way to present the information in a way that presents a high-level summary, using icons and one- or two-word descriptions above but revealing more information when clicked.

Our current design for this information, with a paragraph describing the eight elements in a table, is included as an upload in PDF and Microsoft Word formats. We are looking for a creative way to display these eight things, showing the detail only when the user wants to see it.

The website is being built in WordPress, using Elementor as a page builder.

We will implement (code) the page, but the winner will be asked to specify the widget or other add-in if one is required.

The design does not need to include a header or footer, we have those.

Target Market(s)

Business executives working in technology

Industry/Entity Type

Any

Number of Pages Required

1 page

Font styles to use
Sans Serif

Requirements
Must have
• A design for the body of the page, but not the header or footer.
Nice to have
• Unique icons or images appropriate for each of the eight things.
Should not have
• A lot of text on one page

```html
<!DOCTYPE html>
<html lang="en">
<head>
<meta charset="utf-8">
<title>ERP Implementations – Eight Things to Get Right</title>
<link rel="stylesheet" href="https://fonts.googleapis.com/css2?family=Poppins:wght@300;400;500;600&display=swap">
<style>
:root{
  --brand:#4a7aa8;
  --ink:#333333;
  --card-bg:#f8f8f8;
  --card-line:#dcdcdc;
  --page:#ffffff;
}
*{box-sizing:border-box;margin:0;padding:0}
html,body{width:982px;height:1200px;overflow:hidden;background:var(--page)}
body{font-family:"Poppins",sans-serif;color:var(--ink);position:relative}
.intro{position:absolute;top:72px;left:0;width:982px;text-align:center}
.intro__title{font-size:34px;font-weight:500;color:var(--brand);line-height:1.2}
.intro__rule{width:65px;height:1.5px;background:var(--brand);margin:12px auto 0}
.intro__subtitle{font-size:24px;font-weight:400;margin-top:24px;line-height:1.2;color:#3a3a3a}
.intro__text{font-size:13px;font-weight:300;line-height:18px;width:880px;margin:14px auto 0;color:#444}
.pillars{position:absolute;left:66px;display:grid;grid-template-columns:repeat(4,196px);column-gap:21px}
.pillars--top{top:367px}
.pillars--bottom{top:743px}
.pillar{height:313px;background:var(--card-bg);border:1px solid var(--card-line);border-top:4px solid var(--brand);text-align:center;position:relative}
.pillar__icon{width:60px;height:55px;border:1.5px solid var(--brand);border-radius:4px;background:#fff;margin:36px auto 0;display:flex;align-items:center;justify-content:center}
.pillar__icon svg{width:32px;height:32px;fill:var(--brand)}
.pillar__name{font-size:16px;font-weight:500;color:var(--brand);margin-top:23px;line-height:1.2}
.pillar__summary{font-size:12.5px;font-weight:300;line-height:18.2px;height:91px;overflow:hidden;padding:0 12px;margin-top:11px;color:#333}
.pillar__button{position:absolute;left:50%;transform:translateX(-50%);top:256px;width:88px;height:27px;background:var(--brand);color:#fff;font-size:12.5px;font-weight:300;line-height:27px;text-decoration:none;font-family:inherit;border:none}
</style>
</head>
<body>
<header class="intro">
  <h1 class="intro__title">ERP Implementations</h1>
  <div class="intro__rule"></div>
  <h2 class="intro__subtitle">Eight Things to Get Right</h2>
  <p class="intro__text">Like the roots and branches of a tree, there are many considerations in an ERP implementation. Focus too much on the minor details, and you can lose sight of the tree.&nbsp; In an ERP implementation, you must get eight major things right to be successful. Ignore any of them, and your implementation will fail. Get them right, and you will likely succeed.</p>
</header>

<section class="pillars pillars--top">
  <article class="pillar">
    <div class="pillar__icon"><svg viewBox="0 0 32 32"><rect x="3" y="14" width="3" height="14"/><rect x="8" y="18" width="3" height="10"/><rect x="13" y="20" width="3" height="8"/><rect x="18" y="23" width="3" height="5"/><rect x="23" y="24" width="3" height="4"/><circle cx="20" cy="10" r="6" fill="none" stroke="#4a7aa8" stroke-width="1.8"/><path d="M24.5 14.5l5 5" stroke="#4a7aa8" stroke-width="2"/><text x="20" y="13" font-size="8" text-anchor="middle" fill="#4a7aa8" font-family="sans-serif">$</text></svg></div>
    <h3 class="pillar__name">Value</h3>
    <p class="pillar__summary">The project must provide value that significantly exceeds potential project costs and should be aligned with the goals of the business.</p>
    <a class="pillar__button" href="#">Learn More</a>
  </article>
  <article class="pillar">
    <div class="pillar__icon"><svg viewBox="0 0 32 32"><circle cx="12" cy="12" r="6"/><circle cx="21" cy="11" r="5"/><circle cx="18" cy="20" r="5"/><circle cx="12" cy="12" r="2.2" fill="#fff"/><circle cx="21" cy="11" r="1.8" fill="#fff"/><circle cx="18" cy="20" r="1.8" fill="#fff"/></svg></div>
    <h3 class="pillar__name">Capability</h3>
    <p class="pillar__summary">The company and the implementation team must be capable of implementing the project on their own or with help.</p>
    <a class="pillar__button" href="#">Learn More</a>
  </article>
  <article class="pillar">
    <div class="pillar__icon"><svg viewBox="0 0 32 32"><circle cx="11" cy="19" r="7"/><circle cx="23" cy="9" r="5"/><circle cx="24" cy="22" r="4"/><circle cx="11" cy="19" r="2.5" fill="#fff"/><circle cx="23" cy="9" r="1.8" fill="#fff"/><circle cx="24" cy="22" r="1.4" fill="#fff"/></svg></div>
    <h3 class="pillar__name">Functionality</h3>
    <p class="pillar__summary">An ERP project must support required business processes, both now and in the future. A systematic review of all processes is needed.</p>
    <a class="pillar__button" href="#">Learn More</a>
  </article>
  <article class="pillar">
    <div class="pillar__icon"><svg viewBox="0 0 32 32"><path d="M8 3h12l6 6v20H8z"/><rect x="11" y="16" width="12" height="1.5" fill="#fff"/><rect x="11" y="20" width="12" height="1.5" fill="#fff"/><rect x="11" y="24" width="12" height="1.5" fill="#fff"/><rect x="17" y="9" width="2" height="4" fill="#fff"/><rect x="20" y="8" width="2" height="5" fill="#fff"/><circle cx="13" cy="11" r="2" fill="#fff"/></svg></div>
    <h3 class="pillar__name">Data</h3>
    <p class="pillar__summary">ERP systems are data-hungry creatures. Please be careful before assuming that because so much data goes into it, the data is clean.</p>
    <a class="pillar__button" href="#">Learn More</a>
  </article>
</section>

<section class="pillars pillars--bottom">
  <article class="pillar">
    <div class="pillar__icon"><svg viewBox="0 0 32 32"><circle cx="14" cy="16" r="10"/><circle cx="14" cy="16" r="4" fill="#fff"/><rect x="20" y="8" width="2" height="16" fill="#fff"/><path d="M22 11h6M22 16h7M22 21h6" stroke="#4a7aa8" stroke-width="1.3"/></svg></div>
    <h3 class="pillar__name">Technology</h3>
    <p class="pillar__summary">What is the platform for the system?&nbsp; Is it offered by a vendor that will be around for as long as your system?&nbsp; Will it scale?</p>
    <a class="pillar__button" href="#">Learn More</a>
  </article>
  <article class="pillar">
    <div class="pillar__icon"><svg viewBox="0 0 32 32"><rect x="12" y="18" width="8" height="11"/><rect x="4" y="22" width="8" height="7" fill="none" stroke="#4a7aa8" stroke-width="1.2"/><rect x="20" y="24" width="8" height="5" fill="none" stroke="#4a7aa8" stroke-width="1.2"/><rect x="15" y="6" width="2" height="10"/><rect x="7" y="12" width="2" height="8"/><rect x="23" y="14" width="2" height="8"/></svg></div>
    <h3 class="pillar__name">Change Leadership</h3>
    <p class="pillar__summary">Change leadership (often called change management) considers the human side of an ERP implementation. Change is hard for people.</p>
    <a class="pillar__button" href="#">Learn More</a>
  </article>
  <article class="pillar">
    <div class="pillar__icon"><svg viewBox="0 0 32 32"><circle cx="16" cy="12" r="9"/><path d="M11 19l-4 11 5-3 3 4 2-9zM21 19l4 11-5-3-3 4-2-9z"/><circle cx="16" cy="12" r="4" fill="#fff"/></svg></div>
    <h3 class="pillar__name">Quality</h3>
    <p class="pillar__summary">Quality is multi-dimen-sional, and it’s more than a measurement; it’s a perception.&nbsp; An ERP needs to be reliable.&nbsp; But poor usability hurts too.</p>
    <a class="pillar__button" href="#">Learn More</a>
  </article>
  <article class="pillar">
    <div class="pillar__icon"><svg viewBox="0 0 32 32"><path d="M6 6L26 26M26 6L6 26" stroke="#4a7aa8" stroke-width="1.5"/><circle cx="16" cy="16" r="6"/><circle cx="16" cy="16" r="2" fill="#fff"/><circle cx="5" cy="5" r="3"/><circle cx="27" cy="5" r="3"/><circle cx="5" cy="27" r="3"/><circle cx="27" cy="27" r="3"/></svg></div>
    <h3 class="pillar__name">Governance</h3>
    <p class="pillar__summary">ERP projects require both management and leadership.&nbsp; Planning, changing plans, communication, decision making and oversight.</p>
    <a class="pillar__button" href="#">Learn More</a>
  </article>
</section>
</body>
</html>
```